依頼詳細
アパートのオーナー様が問合せをしたくなるデザインで
シンプルで、誠実感のあるデザイン。
記載項目
カナメリビング株式会社 岐阜県関市桜台3丁目4-27
スミカネットFC岐阜北店、スミカネットFC各務原21号店、スミカネットFC関店経営。
電話番号0575-38-4716
×
東和住まいリンク株式会社
全国で社宅代行を受託
社宅として、一括借上
サイズ
A4
ページ数
片面
希望イメージ
シンプル 複雑
単色 カラフル
暗い 明るい
日常 高級
遊び心 厳粛
未来的 伝統的
女性的 男性的
希望する色
赤系、青系
納品ファイル
補足説明
添付は会社のいままで作成したチラシ
参考にはしなくてもいいです。
会社の情報のみ参考
■ 選んだ理由

シンプルですが、買取・管理の区別がはっきりしていて分かりやすい。
色合いも、きれいです。

■ 提案者全員のお礼・コメント

この度は、お時間を割いて多数の応募ありがとうございます。
皆様のご提案はそれぞれの良さがあり、大変悩みました。
私の分かりにくい説明でも、ここまで仕上げるのは見事です。
また、機会がありましたら是非お願い致します。

```html
<!DOCTYPE html>
<html lang="ja">
<head>
<meta charset="utf-8">
<title>物件の買取・管理いたします。</title>
<link rel="stylesheet" href="https://fonts.googleapis.com/css2?family=Noto+Sans+JP:wght@400;500;700;900&display=swap">
<style>
:root{
  --navy:#17337f;
  --blue:#2458b5;
  --sky:#e8f0fa;
  --red:#d6262d;
  --ink:#222;
  --gray:#f3f4f6;
  --white:#fff;
}
*{margin:0;padding:0;box-sizing:border-box}
html,body{width:849px;height:1200px;overflow:hidden;background:var(--white)}
body{font-family:"Noto Sans JP",sans-serif;color:var(--ink)}
.flyer{position:relative;width:849px;height:1200px;overflow:hidden;background:var(--white)}

.header{position:absolute;left:0;top:0;width:849px;height:96px;border-bottom:4px solid var(--navy)}
.notice{position:absolute;left:20px;top:20px;display:flex;align-items:center}
.notice-type{background:var(--navy);color:var(--white);font-size:13px;font-weight:700;line-height:1.2;padding:8px 8px;text-align:center}
.notice-text{border:2px solid var(--navy);color:var(--navy);font-size:13px;font-weight:700;line-height:1.3;padding:6px 10px;background:var(--white);white-space:nowrap}
.headline{position:absolute;right:20px;top:22px;font-size:38px;font-weight:900;color:var(--navy);letter-spacing:1px;white-space:nowrap}

.hero{position:absolute;left:0;top:100px;width:849px;height:368px}
.hero-building{position:absolute;left:250px;top:0;width:599px;height:368px;background:linear-gradient(180deg,#cfe0f3 0%,#eef2f6 45%,#b9bec6 100%)}
.hero-person{position:absolute;left:0;top:0;width:270px;height:368px;background:linear-gradient(180deg,#f1ece6 0%,#e2d5c6 60%,#d7cbbb 100%)}
.hero-catch{position:absolute;right:24px;top:16px;color:var(--red);font-size:24px;font-weight:900;background:rgba(255,255,255,.85);padding:2px 10px}
.hero-copy{position:absolute;left:230px;top:118px;width:600px}
.hero-line1{font-size:62px;font-weight:900;color:var(--navy);text-shadow:0 0 6px #fff,0 0 6px #fff;letter-spacing:2px}
.hero-line2{display:flex;align-items:flex-end;margin-top:10px;margin-left:90px}
.hero-line2 .lead{font-size:36px;font-weight:900;color:var(--navy);text-shadow:0 0 6px #fff,0 0 6px #fff;margin-bottom:8px}
.guarantee{position:relative;margin-left:10px;background:var(--red);color:var(--white);font-size:58px;font-weight:900;padding:2px 14px;line-height:1.2}
.guarantee-tag{position:absolute;right:-4px;background:var(--white);color:var(--red);border:2px solid var(--red);font-size:14px;font-weight:700;padding:0 6px;line-height:1.4}
.guarantee-tag.top{top:-26px}
.guarantee-tag.bottom{bottom:-26px}

.band{position:absolute;left:0;width:849px;height:50px;background:var(--blue);color:var(--white);font-size:28px;font-weight:900;text-align:center;line-height:50px;letter-spacing:3px}
.band.merit{top:476px}

.merits{position:absolute;left:20px;top:540px;width:809px;display:flex;gap:11px}
.merit-card{flex:1;border:2px solid var(--blue);background:var(--white);height:160px}
.merit-title{background:var(--navy);color:var(--white);font-size:20px;font-weight:900;text-align:center;padding:6px 0;white-space:nowrap}
.merit-body{font-size:13px;line-height:1.6;padding:10px 12px;color:var(--ink)}
.merit-body strong{display:block;color:var(--red);font-size:22px;font-weight:900;margin-top:2px}

.plan-head{position:absolute;left:0;top:716px;width:849px;text-align:center;font-size:36px;font-weight:900;color:var(--navy)}
.plan-head .num{color:var(--red);font-size:46px}
.plans{position:absolute;left:20px;top:782px;width:809px;display:flex;gap:14px}
.plan-card{flex:1;border:2px solid var(--blue);height:116px;background:var(--sky);overflow:hidden}
.plan-title{background:var(--blue);color:var(--white);font-size:19px;font-weight:700;padding:4px 10px;white-space:nowrap}
.plan-title small{font-size:12px;font-weight:500}
.plan-body{display:flex;align-items:center;justify-content:center;gap:8px;height:78px;color:var(--navy)}
.plan-label{font-size:16px;font-weight:700;line-height:1.3;white-space:nowrap}
.plan-body .rate{color:var(--red);font-size:48px;font-weight:900;line-height:1}
.plan-note{position:absolute;left:20px;top:904px;font-size:11px;color:#555}

.promise{position:absolute;left:20px;top:924px;width:809px;height:50px;display:flex;align-items:center;justify-content:center;border-top:2px solid var(--red);border-bottom:2px solid var(--red);gap:14px}
.promise .a{font-size:24px;font-weight:900;color:var(--navy)}
.promise .b{font-size:28px;font-weight:900;color:var(--red)}

.footer{position:absolute;left:0;top:988px;width:849px;height:212px;background:var(--gray)}
.partner{position:absolute;left:20px;top:16px;width:210px;height:180px;border:2px solid var(--navy);background:var(--white);padding:14px 10px}
.partner-name{display:flex;align-items:center;gap:6px;font-size:12px;font-weight:700;color:var(--navy);white-space:nowrap}
.partner-name .mark{width:12px;height:12px;background:var(--navy);flex:none}
.partner-x{text-align:center;font-size:20px;font-weight:700;color:var(--navy);margin:10px 0}
.partner-points{background:var(--navy);color:var(--white);font-size:14px;font-weight:700;line-height:1.7;padding:10px 10px;white-space:nowrap}
.contact{position:absolute;left:250px;top:14px;width:578px}
.contact-lead{font-size:15px;font-weight:700;color:var(--navy)}
.phone{display:flex;align-items:center;gap:8px;margin-top:4px}
.phone-num{font-size:56px;font-weight:900;color:var(--navy);letter-spacing:1px;line-height:1.1}
.company-row{display:flex;justify-content:space-between;align-items:flex-start;margin-top:10px}
.company-name{font-size:26px;font-weight:900;color:var(--ink);white-space:nowrap}
.address{font-size:13px;margin-top:4px}
.stores{font-size:12px;line-height:1.6;border-left:3px solid var(--red);padding-left:8px;white-space:nowrap}
.stores-label{font-weight:700;color:var(--red)}
</style>
</head>
<body>
<div class="flyer">

  <header class="header">
    <div class="notice">
      <div class="notice-type">アパート<br>マンション</div>
      <div class="notice-text">オーナー様へ<br>嬉しいお知らせ</div>
    </div>
    <h1 class="headline">物件の買取・管理いたします。</h1>
  </header>

  <section class="hero">
    <div class="hero-building" role="img" aria-label="青空の下に建つ集合住宅の写真"></div>
    <div class="hero-person" role="img" aria-label="スーツ姿で微笑む女性スタッフの写真"></div>
    <div class="hero-catch">空室つくりません!</div>
    <div class="hero-copy">
      <div class="hero-line1">その空き物件、</div>
      <div class="hero-line2">
        <span class="lead">当社につき</span>
        <span class="guarantee">満室保証
          <span class="guarantee-tag top">満室</span>
          <span class="guarantee-tag bottom">満室</span>
        </span>
      </div>
    </div>
  </section>

  <h2 class="band merit">当社の買取メリット</h2>

  <section class="merits">
    <div class="merit-card">
      <div class="merit-title">秘密厳守</div>
      <p class="merit-body">当社が直接買取するため、売却の情報が外部に漏れる心配はありません。</p>
    </div>
    <div class="merit-card">
      <div class="merit-title">適正価格</div>
      <p class="merit-body">地域の相場を熟知した担当者が、適正な価格で査定いたします。</p>
    </div>
    <div class="merit-card">
      <div class="merit-title">実績豊富</div>
      <p class="merit-body">岐阜県内で25年以上の実績<strong>入居率98%</strong></p>
    </div>
    <div class="merit-card">
      <div class="merit-title">早期契約・決済可</div>
      <p class="merit-body">ご相談から最短1週間で契約・決済が可能です。</p>
    </div>
  </section>

  <h2 class="plan-head">管理は、<span class="num">3</span>タイプご用意</h2>

  <section class="plans">
    <div class="plan-card">
      <div class="plan-title">一般管理</div>
      <div class="plan-body"><span class="plan-label">管理料は<br>収納賃料の</span><span class="rate">3%</span></div>
    </div>
    <div class="plan-card">
      <div class="plan-title">サブリース<small>(家賃保証無し)</small></div>
      <div class="plan-body"><span class="plan-label">管理料は<br>収納賃料の</span><span class="rate">5%</span></div>
    </div>
    <div class="plan-card">
      <div class="plan-title">サブリース<small>(家賃保証有り)</small></div>
      <div class="plan-body"><span class="plan-label">管理料は</span><span class="rate">無料</span></div>
    </div>
  </section>
  <p class="plan-note">※管理料は税別となります。詳しくはお問い合わせください。</p>

  <div class="promise">
    <span class="a">仲介に自信あり!</span>
    <span class="b">空室の満室保証お付けします!</span>
  </div>

  <footer class="footer">
    <div class="partner">
      <div class="partner-name"><span class="mark"></span>東和住まいリンク株式会社</div>
      <div class="partner-x">×</div>
      <div class="partner-points">全国で社宅代行を受託<br>社宅として、一括借上</div>
    </div>
    <div class="contact">
      <p class="contact-lead">お気軽にお問い合わせください。お待ちしております!</p>
      <div class="phone">
        <svg width="52" height="52" viewBox="0 0 24 24" aria-hidden="true">
          <circle cx="12" cy="12" r="12" fill="#17337f"/>
          <path d="M8.6 5.8l1.8 2.9c.2.4.1.8-.2 1.1l-1 1c.8 1.6 2 2.8 3.6 3.6l1-1c.3-.3.8-.4 1.1-.2l2.9 1.8c.4.2.5.7.3 1.1l-.9 1.5c-.3.5-.9.8-1.5.7C10.7 17.6 6.4 13.3 5.7 8.3c-.1-.6.2-1.2.7-1.5l1.5-.9c.3-.2.5-.2.7-.1z" fill="#fff"/>
        </svg>
        <span class="phone-num">0575-38-4716</span>
      </div>
      <div class="company-row">
        <div>
          <div class="company-name">カナメリビング株式会社</div>
          <div class="address">岐阜県関市桜台3丁目4-27</div>
        </div>
        <div class="stores">
          <div class="stores-label">直営店</div>
          スミカネットFC岐阜北店<br>
          スミカネットFC各務原21号店<br>
          スミカネットFC関店
        </div>
      </div>
    </div>
  </footer>

</div>
</body>
</html>
```